LORM Business Card Design Project

Company Name: LORM (Bright Harbor Computing Solutions) PGH.
Office Address: Office No 718, Saffron Crest Tower, Palmwood Garden Heights, Dubai, U.A.E
Company line of business:
1) Currently we have a POS solution for retail outlets like duty free shops, supermarkets, department stores etc... The solution is deployed in Coastline Travel Retail on 350 POS and in Sandgate Airport Retail on 100 POS. So our main line of business is the deployment of this solution in retail outlets locally or regionally. We have already deployed the solution in India and Australia.
2) Integration of other third party POS systems with an online credit authorization netwotk in the UAE. This will enable POS applications to connect directly to the acquiring banks without needing an EFT terminal like Paxtrel or Movarski. The credit card payment is completed at the POS.
3) Other solutions that are targeting retail outlets like mobile POS, queue busting solutions, stock taking solutions using hand held devices, transaction capture systems, etc...
4) Other IT services like support of call center solutions from Northwind Callworks and development of new solutions as per customer requirements.
We need a business card design for the company. We don't have any specific requirements and will eave up to the designers to come up with creative designs. At the moment we still don't have a letter head design and the only thing that we have is the company logo that we will upload shortly.
Updates
Dear All,
I just uploaded the logo source files. I am sorry for the delay.
Regards
Samir Odwani
I would like the business cards to have the following details:
Company Tel No
Company Fax No
Company Website Address
Employee Name
Employee Title
Employee Mobile Number
Employee Email Address

```html
<!DOCTYPE html>
<html lang="en">
<head>
<meta charset="utf-8">
<title>LORM Business Card</title>
<link rel="stylesheet" href="https://fonts.googleapis.com/css2?family=Saira:wght@300;400;600&display=swap">
<style>
  :root {
    --stage: #000000;
    --paper: #ffffff;
    --ink: #2a2a2a;
    --ink-soft: #4a4a4a;
    --icon-blue: #1e7fc4;
    --dark-card-center: #3b3b3b;
    --dark-card-edge: #1d1d1d;
    --mark-dot: #b9d02a;
    --corner-light: #e4e4e4;
    --corner-lime: #bfd630;
    --corner-blue: #2387d2;
  }
  * { margin: 0; padding: 0; box-sizing: border-box; }
  html, body {
    width: 1200px; height: 900px; overflow: hidden;
    background: var(--stage);
    font-family: "Saira", Arial, sans-serif;
  }
  .stage { position: relative; width: 1200px; height: 900px; }
  .card {
    position: absolute; top: 276px;
    width: 482px; height: 275px; overflow: hidden;
  }
  .card--front { left: 102px; background: var(--paper); }
  .card--back {
    left: 619px;
    background: radial-gradient(circle at 45% 45%, var(--dark-card-center) 0%, var(--dark-card-edge) 75%);
  }
  .brand {
    position: absolute; display: flex; align-items: center; gap: 10px;
    font-weight: 400; font-size: 44px; letter-spacing: 1px; line-height: 1;
  }
  .card--front .brand { right: 34px; top: 50px; color: var(--ink); }
  .card--back .brand { left: 150px; top: 100px; color: var(--paper); }
  .brand__dot {
    width: 22px; height: 22px; border-radius: 50%; background: var(--mark-dot);
  }
  .person { position: absolute; left: 25px; top: 106px; color: var(--ink); }
  .person__name { font-weight: 600; font-size: 15px; line-height: 1.1; }
  .person__title { font-weight: 400; font-size: 7.5px; color: var(--ink-soft); }
  .address {
    position: absolute; left: 26px; top: 158px;
    font-size: 10.5px; line-height: 16px; color: var(--ink-soft); font-weight: 400;
  }
  .contacts {
    position: absolute; left: 24px; top: 192px; list-style: none;
    font-size: 10.5px; line-height: 15.5px; color: var(--ink-soft);
  }
  .contacts li { display: flex; align-items: center; gap: 5px; }
  .contacts svg { width: 11px; height: 11px; fill: none; stroke: var(--icon-blue); stroke-width: 1.4; }
  .corner-art { position: absolute; left: 0; top: 0; width: 482px; height: 275px; }
</style>
</head>
<body>
<main class="stage">

  <section class="card card--front" aria-label="Business card front">
    <div class="brand"><span class="brand__dot"></span><span class="brand__name">LORM</span></div>

    <div class="person">
      <p class="person__name">Samir Odwani</p>
      <p class="person__title">Senior Manager, Supply Chain</p>
    </div>

    <p class="address">Office No 718, Saffron Crest Tower,<br>Palmwood Garden Heights, Dubai, U.A.E</p>

    <ul class="contacts">
      <li><svg viewBox="0 0 12 12"><rect x="1" y="2.5" width="10" height="7"/><path d="M1 2.5 L6 6.5 L11 2.5"/></svg>sodwani@lorm.com</li>
      <li><svg viewBox="0 0 12 12"><rect x="1.5" y="5" width="9" height="5.5"/><path d="M3.5 5 V1.5 H8.5 V5"/></svg>(305)555-0142 Ext.4816</li>
      <li><svg viewBox="0 0 12 12"><path d="M2 4 C2 2 10 2 10 4 L8.5 5 L7.5 4 H4.5 L3.5 5 Z M3.5 6 H8.5 L9.5 10 H2.5 Z"/></svg>(786)555-0187</li>
      <li><svg viewBox="0 0 12 12"><circle cx="6" cy="6" r="4.5"/><path d="M1.5 6 H10.5 M6 1.5 C3.5 4 3.5 8 6 10.5 M6 1.5 C8.5 4 8.5 8 6 10.5"/></svg>www.lorm.com</li>
    </ul>

    <svg class="corner-art" viewBox="0 0 482 275" role="img" aria-label="Decorative page-curl artwork in the corner">
      <defs>
        <linearGradient id="front-corner" x1="0" y1="1" x2="1" y2="0">
          <stop offset="0" stop-color="var(--corner-light)"/>
          <stop offset="0.55" stop-color="var(--corner-lime)"/>
          <stop offset="1" stop-color="var(--corner-blue)"/>
        </linearGradient>
      </defs>
      <path d="M482,165 C430,215 360,255 270,275 L482,275 Z" fill="url(#front-corner)"/>
    </svg>
  </section>

  <section class="card card--back" aria-label="Business card back">
    <div class="brand"><span class="brand__dot"></span><span class="brand__name">LORM</span></div>

    <svg class="corner-art" viewBox="0 0 482 275" role="img" aria-label="Decorative page-curl artwork in the corner">
      <defs>
        <linearGradient id="back-corner" x1="0" y1="1" x2="1" y2="0">
          <stop offset="0" stop-color="var(--corner-light)"/>
          <stop offset="0.55" stop-color="var(--corner-lime)"/>
          <stop offset="1" stop-color="var(--corner-blue)"/>
        </linearGradient>
      </defs>
      <path d="M482,165 C430,215 360,255 270,275 L482,275 Z" fill="url(#back-corner)"/>
    </svg>
  </section>

</main>
</body>
</html>
```